Brookfarrow Osteopathy and dry needling business card

Business card for Brookfarrow Osteopathy and Dry Needling.

Industry/Entity Type

Health

Contact Information for Business Card

I do not have a phone number yet. I also do not have an email address yet. The physical address is: 48 Lower Crane Street Brookfarrow The website is: www.brookfarrowosteosteopathy.example My details are: Dr Martin Pellowe, Osteopath (B.Clin.Sci (Ost) M.Ost BSC ECON (Hons)

Colors
0094D4
00A9DD
6FCCEA
C7EBF8
E9F6FB

Requirements
Must have
• logo on the back
Nice to have
• Maybe a space for me to write an appointment time and date on the card.

```html
<!DOCTYPE html>
<html lang="en">
<head>
<meta charset="utf-8">
<title>Brookfarrow Osteopathy and Dry Needling – Business Card</title>
<link href="https://fonts.googleapis.com/css2?family=Inter:wght@300;400;600&family=Montserrat:wght@300;400;500&display=swap" rel="stylesheet">
<style>
  :root {
    --backdrop: #b6b6b6;
    --navy: #004a69;
    --white: #ffffff;
    --ink: #1c2a33;
    --accent: #f7963a;
    --brand-blue: #0094d4;
  }
  * { box-sizing: border-box; margin: 0; padding: 0; }
  html, body { width: 1200px; height: 1200px; overflow: hidden; }
  body {
    background: var(--backdrop);
    position: relative;
    font-family: "Montserrat", sans-serif;
    color: var(--ink);
  }
  .card {
    position: absolute;
    left: 179px;
    width: 861px;
    height: 495px;
    overflow: hidden;
    box-shadow: 0 14px 24px rgba(0,0,0,0.28);
  }
  .card--front { top: 84px; background: var(--navy); }
  .card--back { top: 621px; background: var(--white); }

  .pattern-fill {
    position: absolute;
    inset: 0;
    background: linear-gradient(135deg, #004b6b 0%, #004766 100%);
  }

  .brand-seal {
    position: absolute;
    border-radius: 50%;
    background: var(--white);
    display: flex;
    align-items: center;
    justify-content: center;
    text-align: center;
    font-family: "Montserrat", sans-serif;
    font-weight: 500;
    color: var(--brand-blue);
    text-transform: uppercase;
    letter-spacing: 0.08em;
    line-height: 1.35;
  }
  .card--front .brand-seal {
    left: 262px; top: 85px; width: 332px; height: 332px;
    font-size: 24px; padding: 40px;
  }
  .card--back .brand-seal {
    left: 585px; top: 25px; width: 248px; height: 248px;
    font-size: 18px; padding: 28px;
  }

  .header-band {
    position: absolute;
    left: 0; top: 0;
    width: 100%; height: 99px;
    overflow: hidden;
  }
  .header-rule {
    position: absolute;
    left: 0; top: 101px;
    width: 100%; height: 4px;
    background: var(--navy);
  }
  .doctor-name {
    position: absolute;
    left: 35px; top: 28px;
    font-family: "Inter", sans-serif;
    font-weight: 600;
    font-size: 35px;
    color: var(--white);
    letter-spacing: -0.01em;
  }

  .contact-accent {
    position: absolute;
    left: 29px; top: 152px;
    width: 3px; height: 191px;
    background: var(--accent);
  }
  .contact-line {
    position: absolute;
    left: 61px;
    font-size: 26px;
    font-weight: 400;
    white-space: nowrap;
    color: var(--ink);
  }
  .contact-line--address { top: 147px; }
  .contact-line--role { top: 220px; }
  .contact-line--credentials { top: 266px; }
  .contact-line--web { left: 103px; top: 312px; }
  .contact-line--web .highlight { color: var(--accent); }

  .contact-icon {
    position: absolute;
    left: 59px;
    width: 30px; height: 30px;
  }
  .contact-icon--web { top: 314px; }

  .appointment-title {
    position: absolute;
    left: 29px; top: 383px;
    font-family: "Inter", sans-serif;
    font-weight: 300;
    font-size: 30px;
    color: var(--navy);
  }
  .appointment-field {
    position: absolute;
    top: 444px;
    font-size: 27px;
    font-weight: 400;
    color: var(--navy);
  }
  .appointment-field--date { left: 29px; }
  .appointment-field--time { left: 433px; }
  .write-line {
    position: absolute;
    top: 470px;
    height: 2px;
    background: var(--navy);
  }
  .write-line--date { left: 104px; width: 320px; }
  .write-line--time { left: 509px; width: 321px; }

  .footer-band {
    position: absolute;
    left: 0; bottom: 0;
    width: 100%; height: 5px;
    background: var(--navy);
  }
</style>
</head>
<body>

  <section class="card card--front">
    <div class="pattern-fill" role="img" aria-label="Faint repeating outline pattern of vertebra shapes on deep navy"></div>
    <div class="brand-seal">Brookfarrow Osteopathy &amp; Dry Needling</div>
  </section>

  <section class="card card--back">
    <div class="header-band">
      <div class="pattern-fill" role="img" aria-label="Faint repeating outline pattern of vertebra shapes on deep navy"></div>
      <h1 class="doctor-name">Dr Martin Pellowe</h1>
    </div>
    <div class="header-rule"></div>

    <div class="brand-seal">Brookfarrow Osteopathy &amp; Dry Needling</div>

    <div class="contact-accent"></div>
    <p class="contact-line contact-line--address">48 Lower Crane Street Brookfarrow</p>
    <p class="contact-line contact-line--role">Osteopath</p>
    <p class="contact-line contact-line--credentials">B.Clin.Sci (Ost) M.Ost BSc Econ (Hons)</p>

    <svg class="contact-icon contact-icon--web" viewBox="0 0 24 24" aria-hidden="true">
      <g stroke="#17384f" stroke-width="1.5" fill="none">
        <circle cx="12" cy="12" r="10"/>
        <ellipse cx="12" cy="12" rx="4.5" ry="10"/>
        <path d="M2 12h20M3.5 7h17M3.5 17h17M12 2v20"/>
      </g>
    </svg>
    <p class="contact-line contact-line--web">www.brookfarrow<span class="highlight">osteosteopathy</span>.example</p>

    <h2 class="appointment-title">Next Appointment</h2>
    <span class="appointment-field appointment-field--date">Date</span>
    <div class="write-line write-line--date"></div>
    <span class="appointment-field appointment-field--time">Time</span>
    <div class="write-line write-line--time"></div>

    <div class="footer-band"></div>
  </section>

</body>
</html>
```